Company Profile to show details our company services, projects, products and locations

Required 20+ pages for the company profile.

I need company profile for our company, we are working in selling/rental diesel generators, the design should introduce the company services and project in a simple, attractive way.

Profile to be sent to customers and should give a brief about company details, projects, services, products and locations.

MVLQ is a complete solution provider for diesel Generator industry supply, installation, testing, commissioning and maintenance with 10 years’ experience.

We are the soul dealer for Halvern Energy Products ranging from (50 KVA up 220KVA) Powered by HVP engine and from (250 KVA to 25000KVA) powered by Brantwell engine. HVP superior Generating sets are produced to the higher quality and are designed to meet UK & International quality standards.

Market competitors to MVLQ: Velmora, PUXO, Kestal Energy....

Market Competitors for HVP: Brantwell, DUV, PH Marlow......

Target Market(s)

Companies in Oil & Gas, Construction, Utilities, Petrochemical......

Industry/Entity Type

Retail

Font styles to use
Sans Serif

Colors

Designer to choose colors to be used in the design.

Requirements
Must have
• Must show mainly that we sell diesel generators under a dealership from HVP and rental of diesel generators for WPN (Eastern Grid Corporation) projects and private sector companies.
Nice to have
• Introduction about MVLQ
• Details about HVP products (Diesel Generators & Light Towers)
• MVLQ Projects
• Pictures
• Services
• Locations for, Showroom & workshop.
• Showroom:
• HVP - POWER SYSTEMS DIVISION
• Velo Drive Plaza
• Prince Nayef Road
• Al Rawdah, Al Khobar 34871
• Workshop:
• MVLQ – HVP POWER SYSTEMS DIVISION
• Sinaiyah Dirwan (Industrial Area)
• Al Hizam, Dharan
• Al Khobar 31487
• Kingdom of Saudi Arabia
• Tel : 00966-3-8417725
• Fax : 00966-3-8417790

```html
<!DOCTYPE html>
<html lang="en">
<head>
<meta charset="utf-8">
<title>MVLQ Company Profile – Projects &amp; Products Spread</title>
<link href="https://fonts.googleapis.com/css2?family=Lato:wght@400;700;900&family=Montserrat:wght@300;400;600&display=swap" rel="stylesheet">
<style>
  :root{
    --bg:#8b8d9a;
    --page:#f1f1f1;
    --band-dark:#2f2f31;
    --band-mid:#6d6e72;
    --band-light:#d6d6d8;
    --accent:#f2ad14;
    --navy:#1d2748;
    --ink:#2a2a2a;
    --white:#ffffff;
    --night:#0c0d10;
  }
  *{box-sizing:border-box;margin:0;padding:0}
  html,body{width:1200px;height:1000px;overflow:hidden}
  body{background:var(--bg);font-family:"Lato",sans-serif;color:var(--ink);position:relative}

  .spread{position:absolute;left:30px;top:290px;width:1140px;height:420px;display:flex;box-shadow:0 18px 40px rgba(0,0,0,.35)}
  .page{position:relative;width:570px;height:420px;background:var(--page);overflow:hidden}
  .page--left{border-right:1px solid #cfcfcf}
  .page-bg{position:absolute;inset:0;width:100%;height:100%}

  .page-title{position:absolute;font-family:"Montserrat",sans-serif;font-weight:300;color:var(--white);letter-spacing:1px;text-transform:uppercase}
  .page--left .page-title{right:22px;top:44px;font-size:30px}
  .page--right .page-title{left:22px;top:18px;font-size:26px}
  .page-subtitle{position:absolute;left:24px;top:52px;font-family:"Montserrat",sans-serif;font-weight:400;font-size:10px;color:var(--white);letter-spacing:1px}

  .brand-mark{position:absolute;display:flex;align-items:center;gap:5px;font-family:"Lato",sans-serif;font-weight:900;font-size:13px;color:var(--navy)}
  .brand-mark .dot{width:22px;height:22px;border-radius:50%;background:var(--navy)}
  .page--left .brand-mark{left:14px;top:118px}
  .page--right .brand-mark{right:12px;top:24px}

  .photo{position:absolute}
  .photo--night-map{left:20px;top:168px;width:380px;height:204px;background:radial-gradient(ellipse at 60% 40%,#3b3322 0%,#141418 45%,var(--night) 100%)}
  .photo--lighting-tower{left:36px;top:110px;width:180px;height:190px;background:linear-gradient(160deg,#f4f4f4 0%,#dcdcdc 55%,#c8c3b6 100%)}
  .photo--generator{left:228px;top:58px;width:316px;height:170px;background:linear-gradient(180deg,#e9a51c 0%,#f3b320 55%,#2a2f3a 85%,#c9c9c9 100%)}

  .projects-table{position:absolute;border-collapse:collapse;font-size:6.2px;line-height:1.2}
  .projects-table th{background:var(--white);color:var(--ink);font-weight:900;text-transform:uppercase;padding:4px 3px;text-align:left}
  .projects-table td{padding:4px 3px;color:var(--ink)}
  .projects-table tbody tr:nth-child(odd) td{background:var(--accent)}
  .projects-table tbody tr:nth-child(even) td{background:rgba(255,255,255,.88)}
  .projects-table--main{left:28px;top:150px;width:358px}
  .table-panel{position:absolute;left:404px;top:100px;width:156px;height:170px;background:var(--white);border:2px solid var(--band-dark)}
  .projects-table--more{left:407px;top:103px;width:150px}

  .section-label{position:absolute;font-family:"Montserrat",sans-serif;font-weight:300;text-transform:uppercase;color:var(--white);font-size:15px;letter-spacing:.5px}
  .section-label--towers{left:40px;top:88px}
  .section-label--generators{left:270px;top:32px;color:var(--band-dark);font-size:17px}

  .products-intro{position:absolute;left:30px;top:312px;width:520px;font-weight:900;font-size:10.5px;line-height:1.25;text-transform:uppercase;color:var(--navy)}

  .page-footer{position:absolute;left:0;right:0;bottom:0;height:44px;border-top:1px solid #bdbdbd;background:var(--page)}
  .quote{position:absolute;top:14px;font-family:"Lato",sans-serif;font-weight:900;font-size:11px;color:var(--navy);letter-spacing:.3px}
  .attribution{position:absolute;top:10px;font-size:7px;line-height:1.3;color:#555}
  .page--left .quote{left:160px}
  .page--left .attribution{left:16px}
  .page--right .quote{right:80px;font-size:8px}
  .page--right .attribution{right:14px;text-align:right}
</style>
</head>
<body>
<main class="spread">

  <section class="page page--left" aria-label="Our projects">
    <svg class="page-bg" viewBox="0 0 570 420" aria-hidden="true">
      <defs>
        <linearGradient id="bandLeft" x1="0" y1="0" x2="1" y2="0">
          <stop offset="0" stop-color="#e2e2e3"/>
          <stop offset=".45" stop-color="#5e5f63"/>
          <stop offset="1" stop-color="#2b2b2d"/>
        </linearGradient>
      </defs>
      <polygon points="0,0 570,0 570,96 160,96 0,150" fill="url(#bandLeft)"/>
      <polygon points="420,376 570,300 570,376" fill="var(--band-light)"/>
    </svg>
    <h2 class="page-title">Our Projects</h2>
    <div class="brand-mark"><span class="dot"></span>MVLQ</div>

    <div class="photo photo--night-map" role="img" aria-label="Night satellite view of the region with city lights"></div>

    <table class="projects-table projects-table--main">
      <thead><tr><th>No.</th><th>Project Name</th><th>Scope of Work</th><th>Value</th><th>Start</th><th>Client</th></tr></thead>
      <tbody>
        <tr><td>1</td><td>Substation Upgrade</td><td>Supply of 500 KVA sets</td><td>1,250,000</td><td>Jan 2016</td><td>Eastern Grid</td></tr>
        <tr><td>2</td><td>Plant Standby Power</td><td>Rental of 1000 KVA units</td><td>980,000</td><td>Mar 2016</td><td>WPN</td></tr>
        <tr><td>3</td><td>Camp Power Supply</td><td>Install and test 250 KVA</td><td>640,000</td><td>Jun 2016</td><td>Private Client</td></tr>
        <tr><td>4</td><td>Grid Support Phase 2</td><td>Rental of 20 gensets</td><td>2,100,000</td><td>Sep 2016</td><td>WPN</td></tr>
        <tr><td>5</td><td>Refinery Backup Power</td><td>Supply and commission sets</td><td>1,480,000</td><td>Feb 2017</td><td>Oil &amp; Gas Co.</td></tr>
        <tr><td>6</td><td>Site Lighting Works</td><td>Rental of light towers</td><td>320,000</td><td>May 2017</td><td>Builder Co.</td></tr>
        <tr><td>7</td><td>Water Plant Standby</td><td>Maintenance of 800 KVA sets</td><td>760,000</td><td>Aug 2017</td><td>Utility Co.</td></tr>
        <tr><td>8</td><td>Hospital Power</td><td>Supply of 220 KVA set</td><td>410,000</td><td>Jan 2018</td><td>Health Dept.</td></tr>
      </tbody>
    </table>

    <div class="table-panel"></div>
    <table class="projects-table projects-table--more">
      <thead><tr><th>No.</th><th>Project</th><th>Scope</th><th>Client</th></tr></thead>
      <tbody>
        <tr><td>9</td><td>Port Expansion</td><td>Rental of 500 KVA</td><td>WPN</td></tr>
        <tr><td>10</td><td>Mall Standby</td><td>Supply of 350 KVA</td><td>Private</td></tr>
        <tr><td>11</td><td>Pipeline Camp</td><td>Rental of 12 sets</td><td>Oil Co.</td></tr>
        <tr><td>12</td><td>Road Project</td><td>Light tower rental</td><td>Builder</td></tr>
        <tr><td>13</td><td>School Campus</td><td>Supply of 100 KVA</td><td>Ministry</td></tr>
        <tr><td>14</td><td>Factory Backup</td><td>Service contract</td><td>Private</td></tr>
      </tbody>
    </table>

    <footer class="page-footer">
      <p class="attribution">Lord Harwick<br>HVP Chairman</p>
      <p class="quote">“ALWAYS LOOKING FOR A BETTER WAY”</p>
    </footer>
  </section>

  <section class="page page--right" aria-label="Our products">
    <svg class="page-bg" viewBox="0 0 570 420" aria-hidden="true">
      <defs>
        <linearGradient id="bandRight" x1="0" y1="0" x2="1" y2="1">
          <stop offset="0" stop-color="#2b2b2d"/>
          <stop offset=".6" stop-color="#5a5b5f"/>
          <stop offset="1" stop-color="#8d8e92"/>
        </linearGradient>
      </defs>
      <polygon points="0,0 570,0 570,300 0,300" fill="#c9c9cb"/>
      <polygon points="0,0 470,0 290,300 0,300" fill="url(#bandRight)"/>
      <polygon points="490,0 570,0 570,80" fill="#ececec"/>
      <polygon points="0,300 570,300 570,376 0,376" fill="var(--page)"/>
    </svg>
    <h2 class="page-title">Our Products</h2>
    <p class="page-subtitle">… MORE THAN 170 ITEMS</p>
    <div class="brand-mark"><span class="dot"></span>MVLQ</div>

    <div class="photo photo--lighting-tower" role="img" aria-label="Mobile lighting tower parked beside a white site building"></div>
    <h3 class="section-label section-label--towers">Lighting Towers</h3>

    <h3 class="section-label section-label--generators">Power Generators</h3>
    <div class="photo photo--generator" role="img" aria-label="Yellow canopied diesel power generator"></div>

    <p class="products-intro">All our models, these machines are designed to meet the rigours of the local environment whilst being easy to maintain and offering a high level of reliability.</p>

    <footer class="page-footer">
      <p class="quote">“ALWAYS LOOKING FOR A BETTER WAY”</p>
      <p class="attribution">Lord Harwick<br>HVP Chairman</p>
    </footer>
  </section>

</main>
</body>
</html>
```